Door Window Cling Design for Self-Storage Business

**Objective:**
Create eye-catching door window clings for two entry doors of our self-storage facility to emphasize our online rental convenience and 24/7 accessibility.

**Key Messages to Include (Please pick one NOT both):**
1. "Rent Online Anytime!"
2. "Always Open Online!"

**Design Requirements:**
- **Visual Elements:** Utilize provided background images (attached) and potentially images from our website (https://www.bramblevaultco.example/locations/dunmore-ga-40582) or Pinlo Venue Listing (https://maplink.example/q/73HxpLd) to create a cohesive design. I have attached a photo of the front of the office door. Please do not use this on the design itself. This photo is intended to show the front office doors.
- **Text:** Ensure clarity and readability of the messages "Rent Online Anytime!" or "Always Open Online!"
- **Branding:** Incorporate our logo and maintain brand colors (blue, gold, and white predominant).
- **Dimensions:** Fit dimensions suitable for standard door window clings (21 inches Wide x 63 inches Tall)

**Target Audience:**
- Local residents seeking storage solutions.
- Businesses needing convenient access to storage options.

**Additional Considerations:**
- Design should be distinct for each door while maintaining a cohesive theme.
- Emphasize ease of online rental and gaining immediate access between 6 AM - 10 PM daily.

**Deliverables:**
- High-resolution digital files compatible with door window cling printing specifications.
- Provide mockups or visual representations for review and approval.

**Additional Notes:**
- Designs should capture attention from a distance and effectively communicate our key messages.
- Creativity in incorporating imagery and text is encouraged to enhance visual appeal and message clarity.

Thank you for your attention to detail. We look forward to seeing your proposed designs for our door window clings!

```html
<!DOCTYPE html>
<html lang="en">
<head>
<meta charset="utf-8">
<title>Kestrel Hill Self Storage – Door Clings</title>
<link href="https://fonts.googleapis.com/css2?family=Poppins:wght@600;700;800&family=Open+Sans:wght@400&display=swap" rel="stylesheet">
<style>
  :root {
    --navy: #0e2a5c;
    --gold: #937352;
    --white: #ffffff;
    --page: #ffffff;
  }
  * { margin: 0; padding: 0; box-sizing: border-box; }
  html, body { width: 914px; height: 1200px; overflow: hidden; background: var(--page); }
  .canvas { position: relative; width: 914px; height: 1200px; }

  .cling {
    position: absolute;
    top: 160px;
    width: 292px;
    height: 878px;
    background: var(--white);
    overflow: hidden;
    font-family: "Poppins", sans-serif;
  }
  .cling--rent { left: 129px; }
  .cling--hours { left: 487px; }

  .cling__art { position: absolute; inset: 0; width: 100%; height: 100%; }

  .brand {
    position: absolute;
    top: 40px;
    left: 0; right: 0;
    text-align: center;
    color: var(--navy);
    font-weight: 700;
    line-height: 1;
  }
  .brand__name { font-size: 22px; letter-spacing: 0.5px; }
  .brand__sub { font-size: 9px; letter-spacing: 4px; margin-top: 6px; }

  .headline-stack {
    position: absolute;
    top: 128px;
    left: 30px;
    font-weight: 800;
    font-size: 43px;
    line-height: 44px;
    letter-spacing: -0.5px;
  }
  .headline-stack .gold { color: var(--gold); }
  .headline-stack .navy { color: var(--navy); }

  .hours-stack {
    position: absolute;
    top: 122px;
    left: 56px;
    width: 180px;
    font-weight: 800;
    text-align: center;
    line-height: 1;
  }
  .hours-stack__lead { color: var(--navy); font-size: 25px; letter-spacing: -0.3px; }
  .hours-stack__main { color: var(--gold); font-size: 46px; letter-spacing: -0.5px; margin-top: 1px; }
  .hours-stack__sub { font-size: 21px; font-weight: 700; margin-top: 14px; letter-spacing: -0.3px; }
  .hours-stack__sub .navy { color: var(--navy); }
  .hours-stack__sub .gold { color: var(--gold); }
  .hours-stack__from {
    display: flex; align-items: center; gap: 10px;
    color: var(--navy); font-size: 15px; font-weight: 700; letter-spacing: 2px;
    margin-top: 2px;
  }
  .hours-stack__from::before, .hours-stack__from::after {
    content: ""; flex: 1; height: 1.5px; background: var(--navy);
  }
  .hours-stack__time { color: var(--gold); font-size: 22px; font-weight: 700; margin-top: 2px; letter-spacing: -0.3px; }
  .hours-stack__daily { color: var(--navy); font-size: 44px; letter-spacing: 9px; margin-top: 4px; margin-right: -9px; }

  .site-url {
    position: absolute;
    bottom: 27px;
    left: 0; right: 0;
    text-align: center;
    color: var(--white);
    font-family: "Open Sans", sans-serif;
    font-size: 12px;
    text-shadow: 0 0 3px rgba(0,0,0,0.7);
  }
</style>
</head>
<body>
<main class="canvas">

  <section class="cling cling--rent">
    <svg class="cling__art" viewBox="0 0 384 1155" preserveAspectRatio="none" aria-hidden="true">
      <defs>
        <linearGradient id="aerialA" x1="0" y1="0" x2="0" y2="1">
          <stop offset="0" stop-color="#6b5c4a"/>
          <stop offset="0.35" stop-color="#8f8a80"/>
          <stop offset="0.7" stop-color="#5d6166"/>
          <stop offset="1" stop-color="#6e6a60"/>
        </linearGradient>
      </defs>
      <path class="band-gold" fill="var(--gold)" d="M0,458 C70,440 150,440 230,478 C300,512 345,532 384,540 V1155 H0 Z"/>
      <path class="band-white" fill="var(--white)" d="M0,478 C80,456 160,468 240,515 C300,550 345,570 384,578 V606 C340,596 290,578 228,545 C155,505 75,480 0,490 Z"/>
    </svg>
    <svg class="cling__art" viewBox="0 0 384 1155" preserveAspectRatio="none" role="img" aria-label="Aerial photograph of the storage facility with rows of unit buildings and parked vehicles">
      <path fill="url(#aerialA)" d="M0,735 C60,670 140,645 210,650 C290,656 350,670 384,682 V1155 H0 Z"/>
    </svg>

    <div class="brand">
      <div class="brand__name">KESTREL HILL</div>
      <div class="brand__sub">SELF STORAGE</div>
    </div>

    <h1 class="headline-stack">
      <span class="gold">RENT</span><br>
      <span class="navy">ONLINE</span><br>
      <span class="gold">ANYTIME!</span>
    </h1>

    <p class="site-url">www.kestrelhillstorage.example</p>
  </section>

  <section class="cling cling--hours">
    <svg class="cling__art" viewBox="0 0 384 1155" preserveAspectRatio="none" aria-hidden="true">
      <defs>
        <linearGradient id="aerialB" x1="0" y1="0" x2="0" y2="1">
          <stop offset="0" stop-color="#5e5446"/>
          <stop offset="0.35" stop-color="#9a9891"/>
          <stop offset="0.7" stop-color="#6d6a63"/>
          <stop offset="1" stop-color="#55575a"/>
        </linearGradient>
      </defs>
      <path class="band-gold" fill="var(--gold)" d="M0,540 C150,536 300,495 384,375 V1155 H0 Z"/>
      <path class="band-white" fill="var(--white)" d="M0,578 C170,575 320,522 384,440 V500 C320,570 170,615 0,615 Z"/>
    </svg>
    <svg class="cling__art" viewBox="0 0 384 1155" preserveAspectRatio="none" role="img" aria-label="Aerial photograph of the storage facility office, parking lot and storage buildings">
      <path fill="url(#aerialB)" d="M0,705 C150,692 300,672 384,640 V1155 H0 Z"/>
    </svg>

    <div class="brand">
      <div class="brand__name">KESTREL HILL</div>
      <div class="brand__sub">SELF STORAGE</div>
    </div>

    <div class="hours-stack">
      <div class="hours-stack__lead">EASY ONLINE</div>
      <div class="hours-stack__main">RENTAL</div>
      <div class="hours-stack__sub"><span class="navy">AND</span> <span class="gold">IMMEDIATE</span></div>
      <div class="hours-stack__from">FROM</div>
      <div class="hours-stack__time">6 AM TO 10 PM</div>
      <div class="hours-stack__daily">DAILY.</div>
    </div>

    <p class="site-url">www.kestrelhillstorage.example</p>
  </section>

</main>
</body>
</html>
```